Website concept design - need very creative and polished web page layouts

Need 3-4 web pages designed (graphic only). Client is an interior designer and has specific design requirements. Need a skilled graphic designer to help me create a concept for the new site.

The site is primarily meant to allow users to build and buy a new product, but should have a portfolio site feel. I have specific requirements so designer won't have to 'figure it out' on their own.

Making use of white space, text orientation, and object movement are essential to the success of this project.

Inspirational sites:

http://brinmoss.example/#en - creative and atypical
https://quolvane.example/ - white space and movement; vertical menu links
https://784k.example- modern into, object hover movement
https://www.tembrosk.example/case-silver-harbor - white space, dimensional feel of objects floating on page; pop of color

Target Market(s)

Interior designers and individuals - both commercial and retail.

Industry/Entity Type

Interior Design

Number of Pages Required

4 page

Font styles to use
Serif
Sans Serif

Requirements
Must have
• Professional design, meet design requirements, professional and highly creative look. This cannot look like or resemble in any way a common or typical website. Making use of white space, text orientation, and object movement are essential to the success of this project.
• Colors for the project:
• COLOR TREATMENT - (Not Final)
• DARK PUTTY – 77% Black
• R 95
• G 96
• B 98
• LIGHT PUTTY – 50% Black
• R 129
• G 131
• B 134
• ** Other Levels of Putty can be used.
• BLUE GREEN - (May not be final)
• R 113
• G 202
• B 210
Should not have
• Cannot look like or resemble a typical website design.

```html
<!DOCTYPE html>
<html lang="en">
<head>
<meta charset="utf-8">
<title>Interior Designer</title>
<link rel="stylesheet" href="https://fonts.googleapis.com/css2?family=Oswald:wght@300;400;500&display=swap">
<style>
:root{
  --putty-dark:#5f6062;
  --putty-mid:#818386;
  --teal:#71cad2;
  --paper:#ffffff;
  --mist:#f3f4f5;
  --ink:#58595b;
}
*{margin:0;padding:0;box-sizing:border-box}
html,body{width:1200px;height:3838px;overflow:hidden}
body{position:relative;background:var(--paper);font-family:"Oswald",sans-serif;color:var(--ink)}
.abs{position:absolute}
.photo{position:absolute;display:block}

/* header */
.hero{left:0;top:0;width:1200px;height:1076px;background:linear-gradient(100deg,#eceef0 0%,#f7f8f9 45%,#ffffff 80%)}
.logo{left:90px;top:50px;font-size:26px;line-height:25px;font-weight:500;color:#3f4042;letter-spacing:-0.5px}
.social-top{left:930px;top:68px;display:flex;gap:14px;font-size:15px;color:var(--putty-dark);line-height:22px}
.menu-btn{left:1058px;top:52px;width:54px;height:54px;border:2px solid #e2e3e4;border-radius:50%;background:#fff}
.hero-title{left:78px;top:206px;font-size:205px;line-height:1;font-weight:400;color:var(--putty-dark);letter-spacing:-2px;z-index:2}
.teal-square{background:var(--teal)}
.hero-square{left:51px;top:371px;width:69px;height:69px;z-index:1}
.link-label{font-size:30px;font-weight:400;color:var(--ink);line-height:1}
.latest{left:339px;top:554px}
.arrow{position:absolute}
.hero-small{left:233px;top:660px;width:271px;height:281px;background:linear-gradient(180deg,#f2f2f0 0%,#e1dfdb 60%,#cfcbc5 100%)}
.hero-big{left:558px;top:371px;width:553px;height:571px;background:linear-gradient(120deg,#3c4040 0%,#5d6260 30%,#c9ccce 60%,#e9ecee 100%);box-shadow:0 60px 50px -30px rgba(0,0,0,.35)}
.hero-down{left:1072px;top:614px;width:82px;height:82px;background:var(--teal)}

/* video band */
.video{left:0;top:1077px;width:1200px;height:620px;background:linear-gradient(110deg,#6ab0dc 0%,#8cc3e3 25%,#a3693c 40%,#ede9e3 55%,#f4f3f1 75%,#d6d6d6 100%)}
.play{left:548px;top:1336px;width:105px;height:105px;background:#333436}

/* about */
.about-title{left:90px;top:1816px;font-size:98px;line-height:86px;font-weight:400;color:var(--putty-dark);text-align:right;width:196px;z-index:2}
.about-square{left:184px;top:1965px;width:41px;height:41px;z-index:1}
.about-rule{left:318px;top:1820px;width:5px;height:194px;background:#e3e4e5}
.about-copy{left:363px;top:1842px;width:750px;font-size:20px;line-height:44px;font-weight:300;color:var(--ink)}
.portfolio{left:131px;top:2250px}
.how{left:681px;top:2250px}
.photo-cafe{left:325px;top:2068px;width:258px;height:430px;background:linear-gradient(180deg,#1f3340 0%,#4c5a5a 35%,#9a6a4a 60%,#c4a07a 80%,#3b3a38 100%)}
.photo-kitchen{left:852px;top:2068px;width:258px;height:430px;background:linear-gradient(180deg,#f1f1f1 0%,#d9d9d9 25%,#2c2b2b 45%,#8a6a45 70%,#3a3a3c 100%)}

/* gallery */
.gallery-band{left:0;top:2605px;width:1200px;height:824px;background:linear-gradient(180deg,#f3f3f3 0%,#f3f3f3 62%,#fbfbfb 66%,#ffffff 100%)}
.gallery-square{left:455px;top:2702px;width:44px;height:44px;z-index:1}
.gallery-title{left:474px;top:2700px;font-size:88px;line-height:1;font-weight:400;color:var(--putty-dark);z-index:2}
.gallery-photo{left:90px;top:2840px;width:750px;height:481px;background:linear-gradient(100deg,#9b4a32 0%,#c87a4a 25%,#5c5d60 50%,#3e3b38 75%,#6c6e70 100%)}
.gallery-cta{left:860px;top:2840px;width:251px;height:481px;background:var(--teal)}
.gallery-cta span{position:absolute;left:36px;top:250px;font-size:46px;line-height:53px;font-weight:500;color:#fff}

/* footer */
.footer{left:0;top:3429px;width:1200px;height:409px;background:var(--putty-dark)}
.footer-line{left:0;top:3552px;width:1200px;text-align:center;font-size:34px;font-weight:500;color:#fff}
.footer-social{left:0;top:3626px;width:1200px;display:flex;justify-content:center;gap:26px;font-size:18px;color:#fff}
.footer-rule{left:0;top:3754px;width:1200px;height:1px;background:#6f7072}
.copyright{left:0;top:3786px;width:1200px;text-align:center;font-size:14px;font-weight:400;color:#fff}
.to-top{left:1133px;top:3728px;width:52px;height:52px;border-radius:50%;background:#fff}
</style>
</head>
<body>

<header>
  <div class="abs hero"></div>
  <div class="abs logo">INTERIOR<br>DESIGNER.</div>
  <nav class="abs social-top"><span>Nuvo</span><span>Tirl</span><span>Gex</span></nav>
  <div class="abs menu-btn">
    <svg width="50" height="50" viewBox="0 0 50 50"><g stroke="#5f6062" stroke-width="2"><line x1="18" y1="19" x2="32" y2="19"/><line x1="18" y1="25" x2="32" y2="25"/><line x1="18" y1="31" x2="32" y2="31"/></g></svg>
  </div>
</header>

<section>
  <div class="abs teal-square hero-square"></div>
  <h1 class="abs hero-title">INTERIOR.</h1>
  <div class="abs link-label latest">Latest Edition</div>
  <svg class="arrow" style="left:446px;top:600px" width="60" height="16" viewBox="0 0 60 16"><g stroke="#71cad2" stroke-width="2" fill="none"><line x1="0" y1="8" x2="57" y2="8"/><polyline points="51,3 57,8 51,13"/></g></svg>
  <div class="photo hero-small" role="img" aria-label="Bright white dining room with pendant lamp and table"></div>
  <div class="photo hero-big" role="img" aria-label="Corner bench seating with grey cushions, round table and window"></div>
  <div class="abs hero-down">
    <svg width="82" height="82" viewBox="0 0 82 82"><g stroke="#fff" stroke-width="2" fill="none"><line x1="41" y1="32" x2="41" y2="50"/><polyline points="35,44 41,50 47,44"/></g></svg>
  </div>
</section>

<section>
  <div class="photo video" role="img" aria-label="Sunlit room corner with wide window of blue sky and wooden frame"></div>
  <div class="abs play">
    <svg width="105" height="105" viewBox="0 0 105 105"><polygon points="46,42 46,63 62,52.5" fill="#fff"/></svg>
  </div>
</section>

<section>
  <div class="abs teal-square about-square"></div>
  <h2 class="abs about-title">ABOUT<br>ME</h2>
  <div class="abs about-rule"></div>
  <p class="abs about-copy">Aenean vulputate eleifend tellus aenean leo ligula porttitor eu consequat vitae eleif-<br>end ac enim aliquam lorem ante dapibus in viverra quis feugiat a tellus phasellus viver<br>rad lorem ipsum.</p>

  <div class="abs link-label portfolio">Full Portfolio</div>
  <svg class="arrow" style="left:231px;top:2292px" width="60" height="16" viewBox="0 0 60 16"><g stroke="#71cad2" stroke-width="2" fill="none"><line x1="0" y1="8" x2="57" y2="8"/><polyline points="51,3 57,8 51,13"/></g></svg>
  <div class="photo photo-cafe" role="img" aria-label="Cosy cafe interior with pendant lights, sofa and wooden tables"></div>

  <div class="abs link-label how">How I did it</div>
  <svg class="arrow" style="left:758px;top:2292px" width="60" height="16" viewBox="0 0 60 16"><g stroke="#71cad2" stroke-width="2" fill="none"><line x1="0" y1="8" x2="57" y2="8"/><polyline points="51,3 57,8 51,13"/></g></svg>
  <div class="photo photo-kitchen" role="img" aria-label="Modern kitchen with dark cabinets, wooden island and bar stools"></div>
</section>

<section>
  <div class="abs gallery-band"></div>
  <div class="abs teal-square gallery-square"></div>
  <h2 class="abs gallery-title">GALLERY</h2>
  <div class="photo gallery-photo" role="img" aria-label="Living room with brick wall, bookshelves, grey sofa and armchair"></div>
  <div class="abs gallery-cta">
    <span>VIEW<br>FULL<br>GALLERY</span>
    <svg class="arrow" style="left:36px;top:425px" width="60" height="16" viewBox="0 0 60 16"><g stroke="#fff" stroke-width="2" fill="none"><line x1="0" y1="8" x2="57" y2="8"/><polyline points="51,3 57,8 51,13"/></g></svg>
  </div>
</section>

<footer>
  <div class="abs footer"></div>
  <p class="abs footer-line">LIKE MY WORK? THEN WHY NOT SHARE IT TOO</p>
  <nav class="abs footer-social"><span>Nuvo</span><span>Tirl</span><span>Gex</span></nav>
  <div class="abs footer-rule"></div>
  <p class="abs copyright">© 2018, ALL RIGHTS REESRVED.</p>
  <div class="abs to-top">
    <svg width="52" height="52" viewBox="0 0 52 52"><g stroke="#5f6062" stroke-width="2" fill="none"><line x1="26" y1="33" x2="26" y2="19"/><polyline points="21,24 26,19 31,24"/></g></svg>
  </div>
</footer>

</body>
</html>
```